Template design for organic gardening site for ShopVantra platform

We need a template design for our new 'Fen Leaf Naturals' shopvantra site. Fen Leaf Naturals specialises in organic nutrients for gardening plus all equipment needed to grow.
Domain name will be www.fenleafnaturals.co.uk
Colours used should include logo colours, see attached image. Other colours to compliment the greens and lift the feel of the site could be yellow or orange.
Home page design should include, but not limited to the following:
Interactive banner carousel space
A smaller banner advertising space
Featured products
New products
Sale products feature/link
Articles links/feature
+ all standard shopvantra features such as menus, etc
The site will be selling products (these are nutrients) such as:
Pelvarimost
Marsh hare soil tonic
Terrawix
Nuro pods
Stem triumph
Sprout charm
Vel
Flint amber
Moswelder
+ more products and brands
Site layouts we like include:
www.tidemarkaquafarm.co.uk ... A bit old fashioned but cool
www.lanternbeds.co.uk ... Nice but too compact
www.flintamber.com ... Has a nice top half
www.sponsorapod.org.uk ... Nice colours and header
www.penhurstplants.co.uk ... nice layout, but needs image carousel
www.wrenmeal.co.uk ... Nice background and colours
www.thistle.co.uk ... Nice colours and layout
www.danielmorrowhorticulture.com ... Nice layout and header
www.sprivant.co.uk ... Cool colours and shop pages layout is nice
www.aquavenor.co.uk ... One of the best layouts
The site should feel clean, modern and elegant.
Target Market(s)
Indoor and outdoor organic gardeners
Look and feel

```html
<!DOCTYPE html>
<html lang="en">
<head>
<meta charset="utf-8">
<title>Fen Leaf Naturals — Home</title>
<link rel="stylesheet" href="https://fonts.googleapis.com/css2?family=Signika:wght@400;600&family=Open+Sans:ital,wght@0,400;0,600;1,400&display=swap">
<style>
:root{
  --green:#7ab530;
  --green-dark:#4b8a36;
  --green-deep:#3f6f2c;
  --cream:#ebe8e0;
  --panel:#e7e4dc;
  --text:#3b3b3b;
  --muted:#777;
  --star:#f2a21b;
  --white:#fff;
}
*{box-sizing:border-box;margin:0;padding:0}
html,body{width:777px;height:1200px;overflow:hidden}
body{position:relative;background:var(--white);font-family:"Open Sans",sans-serif;color:var(--text);font-size:7px}
.abs{position:absolute}
h2,h3,.head{font-family:"Signika",sans-serif}

/* header */
.topband{left:0;top:0;width:777px;height:85px;background:var(--cream)}
.deco{background:linear-gradient(90deg,#5a9a3a,#7ab530);border-radius:14px;opacity:.85}
.logo{left:363px;top:4px;width:52px;height:52px;background:var(--white);border-radius:4px;padding:3px;z-index:3}
.logo div{width:100%;height:100%;background:var(--green-dark);border-radius:3px;display:flex;align-items:center;justify-content:center;color:#fff;font-family:"Signika",sans-serif;font-size:6px;text-align:center;line-height:1.1;font-weight:600}
.contact-top{left:528px;top:14px;font-size:6px;color:#555;line-height:15px}
.contact-top svg{vertical-align:-2px;margin-right:5px}
.nav{left:60px;top:47px;width:656px;height:39px;background:var(--green-dark);border-radius:3px}
.nav ul{list-style:none;display:flex;position:absolute;left:127px;top:17px;gap:25px}
.nav li{color:#fff;font-family:"Signika",sans-serif;font-size:8.5px;font-weight:600}
.nav li.active{color:#b9e070}
.nav li.active::after{content:"";display:block;height:3px;background:var(--green);margin-top:7px}
.nav .icons{right:16px;top:13px}

/* sidebar */
.side{left:60px;width:170px;background:var(--panel)}
.side-title{background:var(--green);color:#fff;font-family:"Signika",sans-serif;font-weight:600;font-size:11px;height:34px;line-height:34px;padding-left:17px}
.newlist{list-style:none;padding:16px 12px 0 12px}
.newlist li{font-size:7px;color:#555;border-bottom:1px solid #d3cfc5;height:17.2px;line-height:17px}
.newlist li:last-child{border:none}
.btn{background:var(--green);color:#fff;font-size:6.5px;text-align:center;border-radius:2px;text-transform:uppercase}
.toprated .item{display:flex;gap:17px;padding:10px 0 0 14px;height:67px}
.toprated .thumb{width:50px;height:50px;border-radius:3px;flex:none}
.toprated .name{font-family:"Signika",sans-serif;color:var(--green);font-size:9.5px;font-weight:600}
.toprated p{font-size:6px;width:68px;line-height:1.3}
.fade{opacity:.35}
.stars{color:var(--star);font-size:6.5px;letter-spacing:1px}
.scroll{left:158px;width:4px;border-radius:2px;background:#d2cec4}

/* banner */
.banner{left:241px;top:97px;width:475px;height:283px;border-radius:3px;background:radial-gradient(ellipse at 40% 35%,#5a5244,#2d2822 70%,#1f1b17)}
.banner h1{position:absolute;top:98px;width:100%;text-align:center;color:#fff;font-family:"Signika",sans-serif;font-weight:600;font-size:29px;letter-spacing:-.3px}
.banner h1 span{color:var(--green)}
.banner p{position:absolute;top:131px;width:100%;text-align:center;color:#fff;font-size:9.5px;line-height:1.3}
.banner .btn{position:absolute;left:189px;top:169px;width:93px;height:22px;line-height:22px;font-size:7px}
.dots{left:221px;top:254px;display:flex;gap:6px}
.dots i{width:6px;height:6px;border-radius:50%;background:#fff;display:block}
.dots i:first-child{background:var(--green)}

/* features */
.feat{top:392px;width:148px;height:34px;border-radius:3px;display:flex;align-items:center;gap:7px;padding-left:4px;color:#fff;white-space:nowrap}
.feat b{font-family:"Signika",sans-serif;font-size:7.5px;font-weight:600;display:block;line-height:1.1}
.feat small{font-size:5.5px;display:block;line-height:1.1}

/* popular */
.sec-title{left:241px;width:475px;text-align:center}
.sec-title h2{color:var(--green-deep);font-size:17px;font-weight:600}
.sec-title p{font-size:7px;color:#555;line-height:1.35;margin-top:3px}
.grid{left:241px;width:475px;display:grid;grid-template-columns:repeat(4,111px);column-gap:10.3px;row-gap:21px}
.card .img{height:80px;border-radius:3px}
.card .row{display:flex;justify-content:space-between;margin-top:2px}
.card .nm{font-size:7px;color:var(--green-deep);font-weight:600;line-height:1}
.card .ml{font-size:6px;color:#888}
.card .price{font-family:"Signika",sans-serif;font-size:13.5px;font-weight:600;color:#222;line-height:1.1}
.card .price sup{font-size:7px}
.card .bot{display:flex;justify-content:space-between;align-items:center;margin-top:1px}
.card .btn{background:var(--green-dark);width:41px;height:11px;line-height:11px;font-size:4.5px}
.loadmore{left:343px;top:766px;width:91px;height:21px;line-height:21px;font-size:7px}

/* newsletter */
.news{left:0;top:808px;width:777px;height:171px;background:var(--cream);text-align:center}
.news h2{margin-top:48px;color:var(--green-deep);font-size:17px;font-weight:600}
.news p{font-size:11.5px;color:#555;margin-top:2px}
.form{left:225px;top:99px;display:flex}
.form .field{width:236px;height:21px;background:#f6f5f2;font-style:italic;color:#aaa;font-size:9px;line-height:21px;text-align:left;padding-left:13px}
.form .btn{width:90px;height:21px;line-height:21px;font-size:7px;border-radius:2px}

/* footer */
.footer{left:0;top:979px;width:777px;height:195px;background:var(--green);color:#fff}
.links{list-style:none;font-size:6px;line-height:16px;text-transform:uppercase}
.fh{font-family:"Signika",sans-serif;font-size:11.5px;font-weight:600}
.footer small{font-size:6px;line-height:1.4;display:block}
.phone{font-family:"Signika",sans-serif;font-size:11px;font-weight:600;letter-spacing:.3px}
.city{font-size:6px;line-height:12.5px}
.brand{display:flex;align-items:center;gap:5px;font-family:"Signika",sans-serif;font-weight:600;font-size:9px}
.brand i{width:16px;height:16px;background:#fff;border-radius:2px;display:block}
.bottom{left:0;top:1174px;width:777px;height:26px;background:var(--green-dark);color:#fff;font-size:6px;text-align:center;line-height:26px}
.bottom span{color:#b9e070}
</style>
</head>
<body>

<header>
  <div class="abs topband"></div>
  <div class="abs deco" role="img" aria-label="Illustrated trees" style="left:86px;top:4px;width:48px;height:44px"></div>
  <div class="abs deco" role="img" aria-label="Butterfly illustrations" style="left:144px;top:12px;width:36px;height:26px"></div>
  <div class="abs deco" role="img" aria-label="Butterfly illustrations" style="left:290px;top:8px;width:46px;height:30px"></div>
  <div class="abs deco" role="img" aria-label="Butterfly illustrations" style="left:440px;top:8px;width:46px;height:30px"></div>
  <div class="abs logo"><div>Fen Leaf<br>Naturals</div></div>
  <div class="abs contact-top">
    <div><svg width="6" height="8" viewBox="0 0 6 8"><path d="M3 0a3 3 0 0 0-3 3c0 2 3 5 3 5s3-3 3-5a3 3 0 0 0-3-3z" fill="#4b8a36"/></svg>c/o Harrow Lane Studios, Fenwick Road 14</div>
    <div><svg width="6" height="7" viewBox="0 0 6 7"><path d="M1 0h2l-1 2 1 2 2 1v2C2 7 0 4 0 1z" fill="#4b8a36"/></svg>555-018-4421 &nbsp;&nbsp;&nbsp; <svg width="8" height="6" viewBox="0 0 8 6"><rect width="8" height="6" fill="#4b8a36"/><path d="M0 0l4 3 4-3" stroke="#fff" fill="none"/></svg>hello@fenleafnaturals.co.uk</div>
  </div>
  <nav class="abs nav">
    <ul>
      <li class="active">HOME</li><li>ABOUT US</li><li>PRODUCTS</li><li>WHY GREEN</li><li>BLOG</li><li>SUPPORT</li><li>CONTACT</li>
    </ul>
    <svg class="abs icons" width="48" height="14" viewBox="0 0 48 14">
      <circle cx="5" cy="6" r="4" stroke="#fff" stroke-width="1.3" fill="none"/><path d="M8 9l3 3" stroke="#fff" stroke-width="1.3"/>
      <path d="M24 3h3l2 7h8l2-5H28" stroke="#fff" stroke-width="1.3" fill="none"/><circle cx="30" cy="12" r="1.2" fill="#fff"/><circle cx="36" cy="12" r="1.2" fill="#fff"/>
      <circle cx="42" cy="4" r="4" fill="#7ab530"/><text x="42" y="6" font-size="5" fill="#fff" text-anchor="middle" font-family="Open Sans">3</text>
    </svg>
  </nav>
</header>

<aside class="abs side" style="top:97px;height:335px">
  <div class="side-title">NEW PRODUCTS</div>
  <ul class="newlist">
    <li>Pelvarimost</li><li>Marsh hare soil tonic</li><li>Terrawix</li><li>Nuro pods</li><li>Stem triumph</li><li>Sprout charm</li><li>Vel</li><li>Flint amber</li><li>Moswelder</li><li>Grow Lights</li><li>Grow Tends</li><li>Pelvarimost</li><li>Marsh hare soil tonic</li><li>Terrawix</li>
  </ul>
  <div class="abs btn" style="left:12px;top:299px;width:91px;height:21px;line-height:21px">More product</div>
</aside>

<aside class="abs side toprated" style="top:459px;height:239px">
  <div class="side-title" style="padding-left:13px">TOP RATE PRODUCTS</div>
  <div class="item"><div class="thumb" role="img" aria-label="Tub of tablet nutrients" style="background:linear-gradient(#f4f4f0,#cfd6c6)"></div><div><div class="name">NURO POD</div><p>Lorem ipsum dolor sit amet,</p><div class="stars">★★★★★</div></div></div>
  <div class="item fade"><div class="thumb" role="img" aria-label="Seedling in soil" style="background:linear-gradient(#f0f0ea,#a9a79e)"></div><div><div class="name">SPROUT CHARM</div><p>Lorem ipsum dolor sit amet,</p><div class="stars">★★★★★</div></div></div>
  <div class="item fade"><div class="thumb" role="img" aria-label="Product packaging" style="background:#c8a460"></div><div><div class="name">FLINT AMBER</div><p>Lorem ipsum dolor sit amet,</p><div class="stars">★★★★★</div></div></div>
  <div class="abs scroll" style="top:45px;height:185px"></div>
  <div class="abs scroll" style="top:45px;height:58px;background:#bdb8ad"></div>
</aside>

<section class="abs banner" role="img" aria-label="Young green seedlings growing in dark soil">
  <h1>GRESS IS ALWAY <span>GREENER</span></h1>
  <p>Lorem ipsum dolor sit amet, consectetur adipiscing elit, sed do eiusmod<br>tempor incididunt ut labore et dolore magna aliqua.</p>
  <div class="btn">READ MORE</div>
  <div class="abs dots"><i></i><i></i><i></i></div>
</section>

<div class="abs feat" style="left:241px;background:var(--green-dark)">
  <svg width="46" height="22" viewBox="0 0 46 22"><rect x="1" y="3" width="28" height="13" fill="#fff"/><path d="M30 7h8l5 5v4H30z" fill="#fff"/><circle cx="9" cy="18" r="3" fill="#fff" stroke="#4b8a36"/><circle cx="36" cy="18" r="3" fill="#fff" stroke="#4b8a36"/></svg>
  <div><b>FREE NEXT DAY DELIVERY</b><small>ON ORDER OVER $25</small></div>
</div>
<div class="abs feat" style="left:405px;background:var(--green);padding-left:9px;gap:14px">
  <span style="width:22px;height:24px;background:#fff;border-radius:3px;display:block"></span>
  <div><b>NOW ACCEPTING Paymora</b><small>A FASTER, SIMPLER WAY TO PLAY</small></div>
</div>
<div class="abs feat" style="left:568px;background:var(--green);padding-left:9px;gap:20px">
  <svg width="22" height="24" viewBox="0 0 22 24"><rect y="3" width="22" height="21" rx="2" fill="#fff"/><rect x="7" y="0" width="8" height="5" fill="#fff"/><path d="M6 14l5-5v3h5v4h-5v3z" fill="#7ab530"/></svg>
  <div><b>NO-QUIBBLE RETURNS</b><small>14 DAY RETURN POLICY</small></div>
</div>

<div class="abs sec-title" style="top:452px">
  <h2>MOST POPULAR PRODUCT</h2>
  <p>Lorem ipsum dolor sit amet, consectetur adipiscing elit, sed do eiusmod<br>tempor incididunt ut labore et dolore magna aliqua.</p>
</div>

<section class="abs grid" style="top:504px">
  <div class="card"><div class="img" role="img" aria-label="Nutrient bottle with fruit label" style="background:linear-gradient(135deg,#2d2f33,#6f7378)"></div><div class="row"><div><div class="nm">Nuro Pod</div><div class="ml">120 ml</div></div><div class="price"><sup>$</sup>250</div></div><div class="bot"><span class="stars">★★★★★</span><span class="btn">Add to card</span></div></div>
  <div class="card"><div class="img" role="img" aria-label="White tub of soil feed" style="background:linear-gradient(#fff,#e6eaf0)"></div><div class="row"><div><div class="nm">Pelvarimost</div><div class="ml">120 ml</div></div><div class="price"><sup>$</sup>69.59</div></div><div class="bot"><span class="stars">★★★★★</span><span class="btn">Add to card</span></div></div>
  <div class="card"><div class="img" role="img" aria-label="Jars of coconut oil" style="background:linear-gradient(#c6834a,#7a4a2a)"></div><div class="row"><div><div class="nm">Essential Coco Oil</div><div class="ml">120 ml</div></div><div class="price"><sup>$</sup>12</div></div><div class="bot"><span class="stars">★★★★★</span><span class="btn">Add to card</span></div></div>
  <div class="card"><div class="img" role="img" aria-label="Cardboard box of nutrient bottles" style="background:linear-gradient(#cdb28c,#b59a74)"></div><div class="row"><div><div class="nm">Try Pack</div><div class="ml">120 ml</div></div><div class="price"><sup>$</sup>22.99</div></div><div class="bot"><span class="stars">★★★★★</span><span class="btn">Add to card</span></div></div>
  <div class="card"><div class="img" role="img" aria-label="Bucket and boxes of growth tablets" style="background:linear-gradient(#3c6b2e,#c98b2d)"></div><div class="row"><div><div class="nm">Stem Triumph</div><div class="ml">120 ml</div></div><div class="price"><sup>$</sup>180</div></div><div class="bot"><span class="stars">★★★★★</span><span class="btn">Add to card</span></div></div>
  <div class="card"><div class="img" role="img" aria-label="Green sprout close up" style="background:radial-gradient(circle at 50% 55%,#8ccf4e,#1f4a1c)"></div><div class="row"><div><div class="nm">Nuro Pod</div><div class="ml">120 ml</div></div><div class="price"><sup>$</sup>16.49</div></div><div class="bot"><span class="stars">★★★★★</span><span class="btn">Add to card</span></div></div>
  <div class="card"><div class="img" role="img" aria-label="Jars of coconut oil" style="background:linear-gradient(#c6834a,#7a4a2a)"></div><div class="row"><div><div class="nm">Essential Coco Oil</div><div class="ml">120 ml</div></div><div class="price"><sup>$</sup>18</div></div><div class="bot"><span class="stars">★★★★★</span><span class="btn">Add to card</span></div></div>
  <div class="card"><div class="img" role="img" aria-label="Cardboard box of nutrient bottles" style="background:linear-gradient(#cdb28c,#b59a74)"></div><div class="row"><div><div class="nm">Try Pack</div><div class="ml">120 ml</div></div><div class="price"><sup>$</sup>40</div></div><div class="bot"><span class="stars">★★★★★</span><span class="btn">Add to card</span></div></div>
</section>
<div class="abs btn loadmore" style="background:var(--green-dark)">Load more</div>

<section class="abs news">
  <h2>JOIN THISTLE CLUB TODAY FOR ACCESS TO EXCLUSIVE BENEFITS</h2>
  <p>Receive monthly inspiration &amp; care tips, plus our latest offers and new products</p>
  <div class="abs form"><div class="field">Email Address</div><div class="btn">Sign up</div></div>
</section>

<footer class="abs footer">
  <ul class="abs links" style="left:101px;top:26px"><li>Plants</li><li>Inspiration</li><li>Wildlife</li><li>The tool shed</li><li>Outdoor living</li><li>Christmas</li><li>Special offers</li><li>Gift vouchers</li></ul>
  <ul class="abs links" style="left:256px;top:26px"><li>Customer service</li><li>Terms and conditions</li><li>Returns policy</li><li>Delivery area and costs</li><li>Gift wrap service</li><li>Free click and collect</li><li>1 year guarantee</li><li>Wholesale</li><li>Affiliate program</li></ul>
  <svg class="abs" style="left:390px;top:31px" width="11" height="12" viewBox="0 0 11 12"><path d="M2 0h3l-1 3 2 3 3 1v3c-5 1-9-4-9-9z" fill="#fff"/></svg>
  <div class="abs fh" style="left:412px;top:28px">CONTACT</div>
  <small class="abs" style="left:412px;top:46px;width:140px">Our Carpark team is with any questions you personally aside</small>
  <div class="abs phone" style="left:412px;top:69px">0800/555 01 77</div>
  <svg class="abs" style="left:391px;top:104px" width="8" height="11" viewBox="0 0 8 11"><path d="M4 0a4 4 0 0 0-4 4c0 3 4 7 4 7s4-4 4-7a4 4 0 0 0-4-4z" fill="#fff"/><circle cx="4" cy="4" r="1.5" fill="#7ab530"/></svg>
  <div class="abs fh" style="left:412px;top:100px">LOCATION</div>
  <div class="abs city" style="left:412px;top:116px">Frankfurt<br>Munich<br>Nuremberg<br>Berlin</div>
  <div class="abs fh" style="left:594px;top:28px">FIND US</div>
  <div class="abs" style="left:594px;top:50px;display:flex;gap:12px">
    <i style="width:9px;height:9px;border-radius:50%;background:#fff;display:block"></i>
    <i style="width:9px;height:9px;border-radius:50%;background:#b9e070;display:block"></i>
    <i style="width:9px;height:9px;border-radius:50%;background:#b9e070;display:block"></i>
    <i style="width:9px;height:9px;border-radius:50%;background:#b9e070;display:block"></i>
  </div>
  <div class="abs brand" style="left:592px;top:77px"><i></i>Fen Leaf Naturals</div>
</footer>
<div class="abs bottom">Imprint &nbsp;|&nbsp; Contact &nbsp;|&nbsp; Terms and Conditions © 2015 <span>Fen Leaf Naturals</span></div>

</body>
</html>
```